The Bayfield Wellness Clinic - Practice Flyer

We need a flyer that generally advertises our services. I've uploaded one old flyer as well as examples of others. I like the style of the materials made by this practice: https://www.facebook.com/PineRidgeCounselingHouse

```html
<!DOCTYPE html>
<html lang="en">
<head>
<meta charset="utf-8">
<title>The Bayfield Wellness Clinic – Practice Flyer</title>
<link rel="stylesheet" href="https://fonts.googleapis.com/css2?family=Libre+Caslon+Text:wght@400;700&family=Montserrat:wght@400;500;600;700&display=swap">
<style>
:root{
  --green:#8ea83a;
  --green-dark:#7a9330;
  --brown:#3a352b;
  --grey:#ebebeb;
  --white:#ffffff;
  --text:#3b3b3b;
  --backdrop:#e7ecec;
}
*{box-sizing:border-box;margin:0;padding:0}
html,body{width:1200px;height:2389px;overflow:hidden;background:var(--backdrop)}
body{font-family:"Montserrat",sans-serif;color:var(--text)}
.flyer{position:absolute;left:40px;top:402px;width:1120px;height:1584px;background:var(--white);overflow:hidden;box-shadow:0 6px 24px rgba(0,0,0,.18)}
.hero-photo{position:absolute;left:0;top:113px;width:1120px;height:650px;
  background:linear-gradient(180deg,#d9d8d4 0%,#bdb8b0 18%,#5b554b 38%,#3f3a32 55%,#6a6358 70%,#4a4339 85%,#2f2a23 100%)}
.brand{position:absolute;left:280px;top:72px;width:560px;height:130px;display:flex;align-items:center;justify-content:center;gap:14px}
.brand-mark{width:22px;height:22px;background:var(--green)}
.brand-name{font-family:"Libre Caslon Text",serif;font-weight:700;font-size:34px;color:var(--brown);background:rgba(255,255,255,.92);padding:14px 26px;white-space:nowrap}
.headline{position:absolute;left:0;top:452px;width:1120px;text-align:center;font-family:"Libre Caslon Text",serif;font-weight:400;color:var(--white);font-size:82px;line-height:84px;letter-spacing:1px}
.rule{position:absolute;left:0;top:768px;width:1120px;height:11px;background:var(--green)}
.seal{position:absolute;left:514px;top:673px;width:94px;height:94px;border-radius:50%;background:var(--white);border:3px solid #e3e3e3}
.seal::after{content:"";position:absolute;left:31px;top:31px;width:26px;height:26px;border-radius:50%;background:var(--green)}
.intro-box{position:absolute;left:79px;top:800px;width:444px;height:275px;background:var(--green);border-radius:16px 0 16px 0;padding:22px 36px;color:var(--white)}
.intro-box h2{font-family:"Libre Caslon Text",serif;font-weight:700;font-size:31px;color:var(--brown);margin-bottom:14px}
.intro-box p{font-weight:700;font-size:13.6px;line-height:18.2px}
.hope{position:absolute;left:551px;top:806px;width:500px;font-size:12.6px;line-height:16px}
.conditions{position:absolute;top:858px;list-style:none;font-size:14px;font-weight:500;line-height:18px}
.conditions.col-a{left:551px;width:200px}
.conditions.col-b{left:790px;width:260px}
.conditions li,.services li{position:relative;padding-left:27px;margin-bottom:9px}
.conditions li::before,.services li::before{content:"";position:absolute;left:0;top:2px;width:14px;height:14px;border-radius:50%;background:var(--brown)}
.conditions li::after,.services li::after{content:"";position:absolute;left:4px;top:5px;width:5px;height:3px;border-left:2px solid var(--white);border-bottom:2px solid var(--white);transform:rotate(-45deg)}
.science{position:absolute;left:79px;top:1084px;width:960px;font-size:13.8px;line-height:18px}
.services-band{position:absolute;left:0;top:1182px;width:1120px;height:345px;background:var(--grey)}
.ribbon{position:absolute;left:320px;top:1190px;width:482px;height:62px}
.ribbon-title{position:absolute;left:320px;top:1198px;width:482px;text-align:center;font-family:"Libre Caslon Text",serif;font-size:38px;color:var(--white)}
.services{position:absolute;top:1268px;list-style:none;font-size:14px;font-weight:600;line-height:17px}
.services li{margin-bottom:17px}
.services.col-a{left:83px;width:480px}
.services.col-b{left:616px;width:400px}
.services.col-b li{margin-bottom:14px}
.divider{position:absolute;left:571px;top:1270px;height:170px;border-left:2px dotted #aaa}
.footer{position:absolute;left:0;top:1527px;width:1120px;height:57px;background:var(--brown)}
.footer-green{position:absolute;left:0;top:1510px;width:500px;height:74px}
.contact{position:absolute;left:78px;top:1508px;color:var(--white)}
.phone{font-weight:700;font-size:38px;line-height:44px;display:flex;align-items:center;gap:6px}
.web{font-weight:700;font-size:17px;display:flex;align-items:center;gap:10px}
.social{position:absolute;left:496px;top:1541px;display:flex;align-items:center;gap:6px;color:var(--white);font-weight:700;font-size:17px}
.social .label{margin-right:8px}
.social .dot{width:24px;height:24px;border-radius:50%;background:var(--white)}
.credit{position:absolute;left:758px;top:1540px;padding-left:14px;border-left:1px solid #8a8578;color:var(--white);font-size:9.5px;line-height:12px}
.credit b{font-weight:700}
</style>
</head>
<body>
<main class="flyer">
  <div class="hero-photo" role="img" aria-label="Misty mountain lake at dawn with forested shores, a small canoe and rocks in the foreground"></div>

  <div class="brand">
    <span class="brand-mark"></span>
    <span class="brand-name">The Bayfield Wellness Clinic</span>
  </div>

  <h1 class="headline">THE BAYFIELD<br>WELLNESS CLINIC</h1>

  <div class="rule"></div>
  <div class="seal"></div>

  <section class="intro-box">
    <h2>Expertise Within Reach</h2>
    <p>The Bayfield Wellness Clinic of Greater Bayfield (BWC) is a multi-site, outpatient behavioral healthcare provider specializing in the evaluation and evidence-based treatment of anxiety disorders, obsessive-compulsive and related disorders, and neurodevelopmental disorders. With locations in New Jersey and telehealth services available across the United States, BWC’s nationally renowned team provides excellence in individualized care.</p>
  </section>

  <p class="hope">Hope starts here. At BWC, we see treatment successes every day – We see people learn to overcome their fears, drop their struggles, and reconnect with what matters most to them. We see people get their lives back.</p>

  <ul class="conditions col-a">
    <li>Anxiety and Panic Disorders</li>
    <li>Phobias</li>
    <li>Posttraumatic Stress Disorder</li>
    <li>Obsessive-Compulsive Disorder</li>
    <li>Trichotillomania, Excoriation Disorder, and other BFRBs</li>
  </ul>
  <ul class="conditions col-b">
    <li>Body Dysmorphic Disorder</li>
    <li>Hoarding Disorder</li>
    <li>Tic and Tourette’s Disorders</li>
    <li>Attention-Deficit / Hyperactivity Disorder</li>
    <li>Learning Disorders</li>
    <li>Disruptive Behavior Disorders</li>
  </ul>

  <p class="science">We value science. We do what works, based on the best available research and scientific evidence, ensuring you receive exceptional care. Beyond the office, BWC clinicians are leaders in the field, providing training and consultation to clinicians and educators around the country.</p>

  <section class="services-band"></section>
  <svg class="ribbon" viewBox="0 0 482 62" aria-hidden="true">
    <path d="M0 0 H30 V8 H452 V0 H482 L466 4 Q452 10 452 24 V50 Q452 62 440 62 H42 Q30 62 30 50 V24 Q30 10 16 4 Z" fill="#3a352b"/>
  </svg>
  <h2 class="ribbon-title">Services We Provide</h2>

  <ul class="services col-a">
    <li>Cognitive Behavioral Therapy</li>
    <li>Exposure and Response Prevention</li>
    <li>Prolonged Exposure</li>
    <li>Cognitive Processing Therapy</li>
    <li>Comprehensive Behavioral Intervention for Tics</li>
    <li>Cognitive Behavioral Therapy for Insomnia</li>
    <li>Psychodynamic &amp; Interpersonal Therapy</li>
  </ul>
  <div class="divider"></div>
  <ul class="services col-b">
    <li>Acceptance and Commitment Therapy</li>
    <li>Organizational Skills Training</li>
    <li>Supportive Parenting for Anxious Childhood Emotions</li>
    <li>Parent Management Training</li>
    <li>Parent-Child Interaction Therapy</li>
    <li>Emotionally Focused Therapy</li>
    <li>Psychological, Psychoeducational, and Forensic Assessment</li>
  </ul>

  <footer class="footer"></footer>
  <svg class="footer-green" viewBox="0 0 500 74" aria-hidden="true">
    <path d="M0 0 H430 L472 74 H0 Z" fill="#8ea83a"/>
    <path d="M434 0 L476 74 H482 L440 0 Z" fill="#ffffff"/>
  </svg>
  <div class="contact">
    <div class="phone">
      <svg width="22" height="24" viewBox="0 0 24 24" aria-hidden="true"><path d="M6.6 10.8a15 15 0 0 0 6.6 6.6l2.2-2.2c.3-.3.7-.4 1-.2 1.1.4 2.3.6 3.6.6.6 0 1 .4 1 1V20c0 .6-.4 1-1 1A17 17 0 0 1 3 4c0-.6.4-1 1-1h3.5c.6 0 1 .4 1 1 0 1.3.2 2.5.6 3.6.1.3 0 .7-.2 1z" fill="#fff"/></svg>
      (555) 014-2290
    </div>
    <div class="web">
      <svg width="18" height="18" viewBox="0 0 20 20" aria-hidden="true"><circle cx="10" cy="10" r="8.5" fill="none" stroke="#fff" stroke-width="1.8"/><ellipse cx="10" cy="10" rx="3.8" ry="8.5" fill="none" stroke="#fff" stroke-width="1.5"/><path d="M1.5 10h17M3 5.5h14M3 14.5h14" stroke="#fff" stroke-width="1.5"/></svg>
      BayfieldWellnessClinic.com
    </div>
  </div>
  <div class="social">
    <span class="label">Find us on</span>
    <span class="dot"></span><span class="dot"></span><span class="dot"></span><span class="dot"></span>
  </div>
  <p class="credit">Elena R. Marsh, PsyD. Licensed Psychologist,<br>Executive Director, <b>Lic. No. 00XX00000000</b></p>
</main>
</body>
</html>
```